Business Card Design

General Brief:
Varnel Works is a newly established international manufacturing company. We have a manufacturing facility in China and are in the process of building a new facility in Brazil and are expanding into Africa, the Middle East and Western markets by marketing our products through a licensee program. We use production line manufacture processes (similar to the automotive industry) to produce houses, apartments, hotels and accommodation for the resource sector. We will need to be able to differentiate between the various regions that we serve and the market we operate in.

Key Words to describe our business:
International, Global, Professional, Quality, Standard Compliant, Designful, Cost Effective, Experienced

General Brief:
We need business card designs which cater for the possibility of differentiating the various regions that we serve and the market we operate in. Also, we need a secondary typography selection which suits the primary typography used in the corporate signature (please always state which font is being applied so as to cross-check for the necessary font licenses). First print will be made for our Chinese head office and division, therefore will have the special prerequisite of featuring two distinct languages: English-speaking and Chinese. We assume that a double sided version (recto/verso) could work best in order to separate the languages—other creative interpretations, options and integrations are welcome.

Logo Symbolism:
A dot might seem to be an unassuming little thing, the first mark on the pristine sheet of paper. In this case, the dot is a beginning. But see what just happened there? The dot, an essential component in the structure of the sentence, closed it, making it a symbol of ending. Therefore, the dot is both an origination and a conclusion, encompassing all the possibilities of the universe within it, a seed full of potential and a symbol of the supreme being. The dot is also called the "bindhu," which means "drop." The bindhu is a symbol of the absolute, marked on the forehead at the position of the third eye in the place believed to be the seat of the soul. The presence of dots outside or within a symbol can signify the presence of something else. It also acts as reminder of the concept of space and all in all performs as a very positive symbol in the Varnel Works logo.

Target Market(s)

See Stationary Project

Industry/Entity Type

Accommodation

Requirements
Must have
• See Stationary Project

Logo on Stationary Project

```html
<!DOCTYPE html>
<html lang="en">
<head>
<meta charset="utf-8">
<title>Varnel Works — Business Card</title>
<link rel="stylesheet" href="https://fonts.googleapis.com/css2?family=Jost:wght@400;500;600;700&display=swap">
<style>
  :root {
    --page-bg: #e8e8ed;
    --card-bg: #f7f8f9;
    --navy: #0c3447;
    --accent-blue: #1f9be0;
    --band-grey: #6e7680;
    --text-body: #1d4557;
  }
  * { margin: 0; padding: 0; box-sizing: border-box; }
  html, body {
    width: 1200px;
    height: 934px;
    overflow: hidden;
    background: var(--page-bg);
    font-family: "Jost", sans-serif;
  }
  .card {
    position: absolute;
    left: 150px;
    top: 210px;
    width: 900px;
    height: 514px;
    background: var(--card-bg);
    box-shadow: 0 18px 40px rgba(40, 45, 60, 0.18);
    overflow: hidden;
  }
  .brand-name {
    position: absolute;
    left: 80px;
    top: 206px;
    font-size: 60px;
    font-weight: 600;
    color: var(--navy);
    letter-spacing: -0.5px;
    line-height: 1;
    white-space: nowrap;
  }
  .holder {
    position: absolute;
    right: 58px;
    top: 62px;
    text-align: right;
    color: var(--navy);
  }
  .holder-name {
    font-size: 27px;
    font-weight: 700;
    letter-spacing: 0.5px;
    line-height: 1;
  }
  .holder-role {
    font-size: 19px;
    font-weight: 400;
    margin-top: 2px;
  }
  .address {
    position: absolute;
    right: 560px;
    top: 378px;
    text-align: right;
    font-size: 19px;
    line-height: 30px;
    color: var(--text-body);
    white-space: nowrap;
  }
  .contact-list {
    position: absolute;
    top: 378px;
    list-style: none;
    font-size: 19px;
    line-height: 30px;
    color: var(--text-body);
    white-space: nowrap;
  }
  .contact-list.online { left: 372px; }
  .contact-list.phones { left: 640px; top: 348px; }
  .contact-list li {
    display: flex;
    align-items: center;
    gap: 12px;
  }
  .icon { width: 20px; height: 20px; flex: none; }
  .band-grey {
    position: absolute;
    left: 0;
    bottom: 0;
    width: 362px;
    height: 36px;
    background: var(--band-grey);
  }
  .band-navy {
    position: absolute;
    left: 368px;
    bottom: 0;
    right: 0;
    height: 36px;
    background: var(--navy);
  }
</style>
</head>
<body>
  <div class="card">
    <div class="brand-name">Varnel Works</div>

    <div class="holder">
      <div class="holder-name">MAREN CALLOWAY</div>
      <div class="holder-role">Manager</div>
    </div>

    <div class="address">
      Harwick Lane<br>
      Millbrook NSW 2190
    </div>

    <ul class="contact-list online">
      <li>
        <svg class="icon" viewBox="0 0 20 20" aria-hidden="true">
          <circle cx="10" cy="10" r="9" fill="none" stroke="var(--accent-blue)" stroke-width="1.4"/>
          <rect x="5" y="6.5" width="10" height="7" fill="none" stroke="var(--accent-blue)" stroke-width="1.3"/>
          <path d="M5 6.8 L10 10.6 L15 6.8" fill="none" stroke="var(--accent-blue)" stroke-width="1.3"/>
        </svg>
        info@varnelworks.com
      </li>
      <li>
        <svg class="icon" viewBox="0 0 20 20" aria-hidden="true">
          <circle cx="10" cy="10" r="8.5" fill="none" stroke="var(--accent-blue)" stroke-width="1.4"/>
          <ellipse cx="10" cy="10" rx="3.6" ry="8.5" fill="none" stroke="var(--accent-blue)" stroke-width="1.2"/>
          <path d="M1.5 10 H18.5 M3 6 H17 M3 14 H17" fill="none" stroke="var(--accent-blue)" stroke-width="1.1"/>
        </svg>
        www.varnelworks.com
      </li>
    </ul>

    <ul class="contact-list phones">
      <li>
        <svg class="icon" viewBox="0 0 20 20" aria-hidden="true">
          <circle cx="10" cy="10" r="9" fill="none" stroke="var(--accent-blue)" stroke-width="1.4"/>
          <path d="M6.4 5.2 L8.2 5 L9 7.6 L7.9 8.5 C8.5 10 9.8 11.4 11.4 12.1 L12.4 11 L15 11.8 L14.8 13.6 C14.6 14.4 13.8 14.8 13 14.7 C9.2 14 6 10.8 5.3 7 C5.2 6.2 5.6 5.4 6.4 5.2 Z" fill="var(--accent-blue)"/>
        </svg>
        +61 2 5550 1400
      </li>
      <li>
        <svg class="icon" viewBox="0 0 20 20" aria-hidden="true">
          <circle cx="10" cy="10" r="9" fill="none" stroke="var(--accent-blue)" stroke-width="1.4"/>
          <rect x="5" y="8.5" width="10" height="5.5" rx="1" fill="var(--accent-blue)"/>
          <rect x="7" y="5.5" width="6" height="3" fill="none" stroke="var(--accent-blue)" stroke-width="1.1"/>
          <rect x="7" y="12" width="6" height="2.5" fill="var(--card-bg)"/>
        </svg>
        +61 2 5550 1410
      </li>
    </ul>

    <div class="band-grey"></div>
    <div class="band-navy"></div>
  </div>
</body>
</html>
```